Bravo Glazing

We need a website design for a company based in Texas that specializes in doors and and windows.
Bravo Glazing is a leading window manufacturer of aluminum and vinyl windows, both serving the replacement and new construction markets. Bravo Glazing Inc. was created over 25 years ago when two existing window manufacturers with excellent reputations in their fields - merged. Bravo Glazing offers a complete line conforming to the needs of residential and commercial window markets.
The final design should be something that communicates professionalism and features they're key value propositions.
Example websites we like:
http://layouts.pebblecraft.example/qx/purse/
http://layouts.pebblecraft.example/qx/splashzone/
http://layouts.pebblecraft.example/qx/refit2/
This design should format the existing content to be more visually organized, improve the fonts to clearer and more readable, and make it easier for users to find services.
Brand guide is attached
Website images can be found here: https://share.vaultdrop.example/7kRtQmZxLpWeYb
Target Market(s)
Windows
Number of Pages Required
1 page
Look and feel
Each slider illustrates characteristics of the customer's brand and the style your logo design should communicate.

```html
<!DOCTYPE html>
<html lang="en">
<head>
<meta charset="utf-8">
<title>Bravo Glazing</title>
<link href="https://fonts.googleapis.com/css2?family=Lora:wght@400;700&family=Roboto:wght@400;500;700&display=swap" rel="stylesheet">
<style>
:root{
  --gold:#d4b24a;
  --gold-dark:#b8972f;
  --maroon:#9f1f3c;
  --ink:#222222;
  --text:#555555;
  --light:#f4f4f4;
  --topbar:#1b1b1b;
  --footer:#2a2622;
  --bottom:#141414;
  --white:#ffffff;
}
*{margin:0;padding:0;box-sizing:border-box}
html,body{width:1200px;height:3416px;overflow:hidden}
body{position:relative;font-family:'Roboto',Arial,sans-serif;color:var(--ink);background:var(--white)}
.abs{position:absolute}
.serif{font-family:'Lora',Georgia,serif}

/* top bar */
.topbar{left:0;top:0;width:1200px;height:36px;background:var(--topbar);color:#ddd;font-size:12px}
.topbar .info{position:absolute;top:11px;display:flex;align-items:center;gap:8px}
.topbar svg{fill:var(--gold)}
.socials{position:absolute;right:150px;top:12px;display:flex;gap:14px}
.socials span{width:11px;height:11px;border-radius:50%;background:#ddd;display:block}

/* header */
.header{left:0;top:36px;width:1200px;height:82px;background:var(--white)}
.logo{position:absolute;left:152px;top:24px;font-family:'Lora',Georgia,serif;font-size:28px;color:var(--gold-dark);font-weight:700}
.nav{position:absolute;right:245px;top:34px;display:flex;gap:22px;font-size:11px;font-weight:700;white-space:nowrap}
.search{position:absolute;left:973px;top:0;width:78px;height:82px;background:var(--gold);display:flex;align-items:center;justify-content:center}

/* hero */
.hero{left:0;top:118px;width:1200px;height:595px;background:linear-gradient(180deg,#6f6a5e 0%,#8c8f7a 30%,#6f7d55 55%,#7a6a55 75%,#5a4c3e 100%)}
.hero-shade{position:absolute;inset:0;background:rgba(0,0,0,.25)}
.hero h2{position:absolute;width:100%;top:166px;text-align:center;color:var(--gold);font-size:25px;font-weight:400;letter-spacing:.5px}
.hero h1{position:absolute;width:100%;top:204px;text-align:center;color:#fff;font-size:25px;font-weight:400;letter-spacing:.5px;font-family:'Roboto',Arial,sans-serif}
.hero p{position:absolute;left:300px;width:600px;top:278px;text-align:center;color:#fff;font-size:11px;line-height:22px;text-transform:uppercase}
.btn{display:flex;align-items:center;justify-content:center;background:var(--gold);color:var(--ink);font-size:14px;font-weight:500}
.hero .btn{position:absolute;left:530px;top:390px;width:142px;height:45px}
.arrow{position:absolute;top:282px;width:40px;height:40px;border:1px solid rgba(255,255,255,.6);display:flex;align-items:center;justify-content:center}

/* features */
.features{left:0;top:713px;width:1200px;height:312px;background:var(--light)}
.feature{position:absolute;top:90px;width:230px;text-align:center}
.feature svg{display:block;margin:0 auto;height:32px}
.feature h3{font-size:14px;font-weight:500;margin-top:28px}
.feature p{font-size:11px;color:var(--text);line-height:20px;margin-top:18px}

/* why */
.why{left:0;top:1025px;width:1200px;height:678px;background:var(--white)}
.why-img{position:absolute;left:150px;top:125px;width:370px;height:460px;background:linear-gradient(160deg,#f7f7f5,#e6e6e2 60%,#d4d4cf)}
.why h2{position:absolute;left:603px;top:98px;color:var(--gold);font-size:28px;font-weight:400}
.rule{height:3px;background:var(--ink)}
.why .rule{position:absolute;left:612px;top:166px;width:64px;height:2px}
.why .intro{position:absolute;left:612px;top:186px;font-size:11px;color:var(--text)}
.point{position:absolute;left:612px;width:440px}
.point .ico{position:absolute;left:0;top:0;width:48px;height:48px;background:var(--ink);border:3px solid var(--gold);display:flex;align-items:center;justify-content:center}
.point h3{position:absolute;left:73px;top:0;font-size:14px;font-weight:500}
.point p{position:absolute;left:73px;top:30px;width:370px;font-size:11px;color:var(--text);line-height:21px}

/* services */
.services{left:0;top:1703px;width:1200px;height:679px;background:var(--gold)}
.sec-title{position:absolute;width:100%;text-align:center;font-size:28px;font-weight:400}
.sec-rule{position:absolute;left:578px;width:44px;height:3px;background:var(--white)}
.sec-sub{position:absolute;width:100%;text-align:center;font-size:10px;color:var(--ink)}
.card{position:absolute;top:224px;width:285px;height:308px;background:var(--white);text-align:center}
.card .photo{height:158px}
.card .tag{position:absolute;left:119px;top:134px;width:47px;height:47px;background:var(--ink);display:flex;align-items:center;justify-content:center}
.card h3{margin-top:36px;font-size:14px;font-weight:500}
.card p{margin:14px 24px 0;font-size:11px;color:var(--text);line-height:21px}

/* partners */
.partners{left:0;top:2382px;width:1200px;height:373px;background:var(--light)}
.partners .sec-rule{background:var(--gold)}
.badge{position:absolute;top:215px;width:110px;height:58px;background:#cfcfcf;border-radius:6px}

/* estimate */
.estimate{left:0;top:2755px;width:1200px;height:221px;background:var(--maroon);color:#fff}
.estimate h3{position:absolute;left:150px;top:89px;font-size:19px;font-weight:500}
.estimate p{position:absolute;left:150px;top:122px;font-size:11px}
.estimate .btn{position:absolute;left:910px;top:87px;width:158px;height:45px}

/* footer */
.footer{left:0;top:2976px;width:1200px;height:367px;background:linear-gradient(180deg,#2b2722,#1f1c19);color:#e8e8e8}
.col{position:absolute;top:64px;width:210px;font-size:11px;line-height:22px}
.col h4{font-size:14px;font-weight:500;margin-bottom:16px;letter-spacing:.3px}
.col .flogo{font-family:'Lora',Georgia,serif;font-size:18px;color:var(--gold);font-weight:700;margin-bottom:12px}
.col ul{list-style:none}
.col li{position:relative;padding-left:22px}
.col li svg{position:absolute;left:0;top:7px}
.fsoc{display:flex;gap:8px;margin-top:20px}
.fsoc span{width:24px;height:24px;border:1px solid var(--gold);display:block}
.bottom{left:0;top:3343px;width:1200px;height:73px;background:var(--bottom);color:#ccc;font-size:11px;display:flex;align-items:center;justify-content:center}
</style>
</head>
<body>

<div class="abs topbar">
  <div class="info" style="left:150px">
    <svg width="12" height="12" viewBox="0 0 24 24"><path d="M6.6 10.8a15 15 0 006.6 6.6l2.2-2.2a1 1 0 011-.25 11 11 0 003.5.55 1 1 0 011 1V20a1 1 0 01-1 1A17 17 0 013 4a1 1 0 011-1h3.5a1 1 0 011 1 11 11 0 00.55 3.5 1 1 0 01-.25 1z"/></svg>
    +1 (512) 555 0147
  </div>
  <div class="info" style="left:290px">
    <svg width="12" height="12" viewBox="0 0 24 24"><circle cx="12" cy="12" r="10" fill="none" stroke="#d4b24a" stroke-width="2.5"/><path d="M12 6v6l4 2" stroke="#d4b24a" stroke-width="2.5" fill="none"/></svg>
    Mon - Sat 12:00 - 20:00
  </div>
  <div class="socials"><span></span><span></span><span></span><span></span><span></span><span></span></div>
</div>

<header class="abs header">
  <div class="logo">Bravo Glazing</div>
  <nav class="nav"><span>HOME</span><span>ABOUT</span><span>SERVICES</span><span>GALLERY</span><span>BLOG</span><span>CONTACT</span></nav>
  <div class="search"><svg width="14" height="14" viewBox="0 0 24 24"><circle cx="10" cy="10" r="7" fill="none" stroke="#fff" stroke-width="3"/><path d="M15 15l6 6" stroke="#fff" stroke-width="3"/></svg></div>
</header>

<section class="abs hero" role="img" aria-label="Sunroom with floor-to-ceiling windows looking out over green fields">
  <div class="hero-shade"></div>
  <h2 class="serif">HIGH PERFORMANCE WINDOWS</h2>
  <h1>DURABLE AND FULLY ENERGY EFFICIENT</h1>
  <p>Lorem ipsum dolor sit amet, consectetur adipiscing elit, sed do eiusmod tempor incididunt ut labore et dolore magna aliqua.</p>
  <div class="btn">OUR PRODUCTS</div>
  <div class="arrow" style="left:82px"><svg width="10" height="12" viewBox="0 0 10 12"><path d="M8 0L0 6l8 6z" fill="#d4b24a"/></svg></div>
  <div class="arrow" style="left:1078px"><svg width="10" height="12" viewBox="0 0 10 12"><path d="M2 0l8 6-8 6z" fill="#d4b24a"/></svg></div>
</section>

<section class="abs features">
  <div class="feature" style="left:135px">
    <svg width="34" height="32" viewBox="0 0 24 22"><path d="M12 1L1 11h3v10h6v-6h4v6h6V11h3z" fill="#d4b24a"/></svg>
    <h3>Residential Projects</h3>
    <p>Lorem ipsum dolor sit amet, consectetur adipiscing elit, sed do eiusmod</p>
  </div>
  <div class="feature" style="left:365px">
    <svg width="28" height="32" viewBox="0 0 20 24"><rect x="1" y="1" width="18" height="22" fill="#d4b24a"/><g fill="#f4f4f4"><rect x="4" y="4" width="3" height="3"/><rect x="9" y="4" width="3" height="3"/><rect x="14" y="4" width="3" height="3"/><rect x="4" y="9" width="3" height="3"/><rect x="9" y="9" width="3" height="3"/><rect x="14" y="9" width="3" height="3"/><rect x="4" y="14" width="3" height="3"/><rect x="14" y="14" width="3" height="3"/><rect x="8" y="17" width="5" height="6"/></g></svg>
    <h3>Commercial Projects</h3>
    <p>Lorem ipsum dolor sit amet, consectetur adipiscing elit, sed do eiusmod</p>
  </div>
  <div class="feature" style="left:601px">
    <svg width="32" height="32" viewBox="0 0 24 24"><circle cx="12" cy="12" r="10" fill="none" stroke="#d4b24a" stroke-width="2.5"/><path d="M12 6v6l4 3" stroke="#d4b24a" stroke-width="2.5" fill="none"/></svg>
    <h3>On Time Delivery</h3>
    <p>Lorem ipsum dolor sit amet, consectetur adipiscing elit, sed do eiusmod</p>
  </div>
  <div class="feature" style="left:833px">
    <svg width="32" height="32" viewBox="0 0 24 24"><path d="M2 10h4v12H2zM8 21V10l5-8c1.5 0 2.5 1 2 3l-1 4h7c1.2 0 2 1 1.8 2.2l-1.6 8A2 2 0 0119.2 21z" fill="#d4b24a"/></svg>
    <h3>Quality Assurance</h3>
    <p>Lorem ipsum dolor sit amet, consectetur adipiscing elit, sed do eiusmod</p>
  </div>
</section>

<section class="abs why">
  <div class="why-img" role="img" aria-label="White sliding glass door product shot"></div>
  <h2 class="serif">WHY OUR PRODUCTS</h2>
  <div class="rule"></div>
  <p class="intro">There are many variations of passages of Lorem Ipsum available.</p>
  <div class="point" style="top:216px">
    <div class="ico"><svg width="18" height="18" viewBox="0 0 24 24"><path d="M21 5a5 5 0 01-7 5L5 19l-2-2 9-9a5 5 0 015-7l-3 3 1 3 3 1z" fill="#d4b24a"/></svg></div>
    <h3>30+ YEARS OF EXPERIENCE</h3>
    <p>Lorem Ipsum is simply dummy text of the printing and typesetting industry. Lorem Ipsum has been the industry's standard dummy text ever since the 1500s</p>
  </div>
  <div class="point" style="top:338px">
    <div class="ico"><svg width="18" height="18" viewBox="0 0 24 24"><path d="M22 2L2 10l8 3 3 8z" fill="#d4b24a"/></svg></div>
    <h3>QUALIFIED EXPERTS</h3>
    <p>Lorem Ipsum is simply dummy text of the printing and typesetting industry. Lorem Ipsum has been the industry's standard dummy text ever since the 1500s</p>
  </div>
  <div class="point" style="top:458px">
    <div class="ico"><svg width="20" height="18" viewBox="0 0 26 22"><circle cx="13" cy="6" r="4" fill="#d4b24a"/><circle cx="5" cy="8" r="3" fill="#d4b24a"/><circle cx="21" cy="8" r="3" fill="#d4b24a"/><path d="M6 20a7 7 0 0114 0zM0 19a5 5 0 016-5zM26 19a5 5 0 00-6-5z" fill="#d4b24a"/></svg></div>
    <h3>BEST CUSTOMER SERVICES</h3>
    <p>Lorem Ipsum is simply dummy text of the printing and typesetting industry. Lorem Ipsum has been the industry's standard dummy text ever since the 1500s</p>
  </div>
</section>

<section class="abs services">
  <h2 class="sec-title serif" style="top:70px">OUR SERVICES</h2>
  <div class="sec-rule" style="top:135px"></div>
  <p class="sec-sub" style="top:162px">LOREM IPSUM IS SIMPLY DUMMY TEXT OF THE PRINTING AND TYPESETTING INDUSTRY</p>
  <div class="card" style="left:150px">
    <div class="photo" role="img" aria-label="Pencil sketch of a house design" style="background:linear-gradient(180deg,#fafafa,#dcdcdc)"></div>
    <div class="tag"><svg width="16" height="16" viewBox="0 0 24 24"><path d="M3 17v4h4L19 9l-4-4zM16 4l4 4 2-2-4-4z" fill="#fff"/></svg></div>
    <h3>DESIGN &amp; PLANNING</h3>
    <p>Lorem Ipsum is simply dummy text of the printing and typesetting industry. Lorem Ipsum has been the industry's standard dummy</p>
  </div>
  <div class="card" style="left:459px">
    <div class="photo" role="img" aria-label="Installer fitting a window frame" style="background:linear-gradient(135deg,#8a3a2e,#c98a6a 50%,#e5e0b0)"></div>
    <div class="tag"><svg width="18" height="14" viewBox="0 0 24 18"><rect x="1" y="1" width="22" height="16" rx="2" fill="none" stroke="#fff" stroke-width="2"/><g fill="#fff"><rect x="4" y="5" width="3" height="2"/><rect x="9" y="5" width="3" height="2"/><rect x="14" y="5" width="3" height="2"/><rect x="6" y="11" width="12" height="2"/></g></svg></div>
    <h3>INSTALLATION</h3>
    <p>Lorem Ipsum is simply dummy text of the printing and typesetting industry. Lorem Ipsum has been the industry's standard dummy</p>
  </div>
  <div class="card" style="left:767px">
    <div class="photo" role="img" aria-label="Worker cleaning sunroom windows" style="background:linear-gradient(180deg,#3f4a55,#8aa0b0 50%,#5c6a5a)"></div>
    <div class="tag"><svg width="16" height="16" viewBox="0 0 24 24"><path d="M4 8l6-6 4 4-2 2 10 10-3 3L9 11l-2 2z" fill="#fff"/></svg></div>
    <h3>MAINTENANCE</h3>
    <p>Lorem Ipsum is simply dummy text of the printing and typesetting industry. Lorem Ipsum has been the industry's standard dummy</p>
  </div>
</section>

<section class="abs partners">
  <h2 class="sec-title serif" style="top:74px">OUR PARTNERS</h2>
  <div class="sec-rule" style="top:124px"></div>
  <p class="sec-sub" style="top:152px">LOREM IPSUM IS SIMPLY DUMMY TEXT OF THE PRINTING AND TYPESETTING INDUSTRY</p>
  <div class="badge" style="left:150px"></div>
  <div class="badge" style="left:350px"></div>
  <div class="badge" style="left:550px"></div>
  <div class="badge" style="left:745px"></div>
  <div class="badge" style="left:940px"></div>
</section>

<section class="abs estimate">
  <h3>Request A Free Estimate</h3>
  <p>Lorem ipsum dolor sit amet, consectetur adipiscing elit, sed do eiusmod tempor incididunt ut labore et dolore magna aliqua.</p>
  <div class="btn">BOOK NOW</div>
</section>

<footer class="abs footer">
  <div class="col" style="left:150px">
    <h4>ABOUT BRAVO GLAZING</h4>
    <div class="flogo">Bravo Glazing</div>
    <p>Lorem ipsum dolor sit amet, consectetur adipiscing elit, sed do eiusmod tempor incididunt ut labore et dolore magna aliqua.</p>
    <div class="fsoc"><span></span><span></span><span></span><span></span></div>
  </div>
  <div class="col" style="left:382px">
    <h4>QUICK LINKS</h4>
    <ul>
      <li><svg width="8" height="8" viewBox="0 0 8 8"><path d="M2 0l4 4-4 4" stroke="#d4b24a" stroke-width="2" fill="none"/></svg>Building Construction</li>
      <li><svg width="8" height="8" viewBox="0 0 8 8"><path d="M2 0l4 4-4 4" stroke="#d4b24a" stroke-width="2" fill="none"/></svg>Home Renovation</li>
      <li><svg width="8" height="8" viewBox="0 0 8 8"><path d="M2 0l4 4-4 4" stroke="#d4b24a" stroke-width="2" fill="none"/></svg>Hardwood Flooring</li>
      <li><svg width="8" height="8" viewBox="0 0 8 8"><path d="M2 0l4 4-4 4" stroke="#d4b24a" stroke-width="2" fill="none"/></svg>Repairing Of Roof</li>
      <li><svg width="8" height="8" viewBox="0 0 8 8"><path d="M2 0l4 4-4 4" stroke="#d4b24a" stroke-width="2" fill="none"/></svg>Commercial Construction</li>
      <li><svg width="8" height="8" viewBox="0 0 8 8"><path d="M2 0l4 4-4 4" stroke="#d4b24a" stroke-width="2" fill="none"/></svg>Concreate Transport</li>
    </ul>
  </div>
  <div class="col" style="left:613px">
    <h4>TWITTER FEED</h4>
    <p>@quartzlane: Duis aute irure dolor in reprehenderit in voluptate velit esse cillum dolore eu fugiat.</p>
    <p style="margin-top:12px">@quartzlane: Duis aute irure dolor in reprehenderit in voluptate velit esse cillum dolore eu fugiat.</p>
  </div>
  <div class="col" style="left:844px">
    <h4>CONTACT US</h4>
    <p>Have questions, comments or just want to say hello:</p>
    <ul style="margin-top:10px">
      <li><svg width="11" height="9" viewBox="0 0 22 16"><rect width="22" height="16" fill="#d4b24a"/><path d="M0 0l11 9 11-9" stroke="#2a2622" stroke-width="2" fill="none"/></svg>hello@bravoglazing.example</li>
      <li><svg width="10" height="10" viewBox="0 0 24 24"><path d="M6.6 10.8a15 15 0 006.6 6.6l2.2-2.2 5.6 1.8V21A17 17 0 013 4h4.8l1.8 5.6z" fill="#d4b24a"/></svg>+1 512 555 0190</li>
      <li><svg width="9" height="11" viewBox="0 0 18 24"><path d="M9 0a9 9 0 019 9c0 7-9 15-9 15S0 16 0 9a9 9 0 019-9z" fill="#d4b24a"/><circle cx="9" cy="9" r="3" fill="#2a2622"/></svg>Suite 12, 480 Mesa Lane, Austin, TX 78701</li>
    </ul>
  </div>
</footer>

<div class="abs bottom">Bravo Glazing. TX. USA. Copyright 2017 - 2018 All rights reserved.</div>

</body>
</html>
```